Foreclosure Postcard for Consumer Attorneys

We are a law firm representing consumers in the areas of bankruptcy and foreclosure. We need a postcard to send to consumers who are already in foreclosure. We want them to know that they have options and that we can help them save their homes. They don't have to lose their homes to the bank. We're looking for designs using the colors red and white and the word "FORECLOSURE" in large print, displayed prominently on the postcard. People in this situation often throw their mail away because they get so many bills. We want this to catch their attention and for them to call us. So we also want our phone number 270-493-2817 displayed prominently.

Target Market(s)

Consumers in Foreclosure

Industry/Entity Type

Law Firm

Font styles to use
Serif
Sans Serif

Requirements
Must have
• Phone number: 270-493-2817
Dranford & Pelk, P.S.C.
428 Harlow Ridge Road
Owensboro, KY 42301

```html
<!DOCTYPE html>
<html lang="en">
<head>
<meta charset="utf-8">
<title>Foreclosure Postcard – Dranford &amp; Pelk, P.S.C.</title>
<link rel="stylesheet" href="https://fonts.googleapis.com/css2?family=Ultra&family=Della+Respira&family=Open+Sans:wght@400&family=Playfair+Display:wght@400&display=swap">
<style>
  :root {
    --paper: #ffffff;
    --ink: #1f2423;
    --headline-top: #f0261f;
    --headline-bottom: #8c0b0b;
    --headline-shadow: #3a0505;
    --brand-ink: #3b3b33;
  }
  * { margin: 0; padding: 0; box-sizing: border-box; }
  html, body { width: 1200px; height: 924px; overflow: hidden; background: var(--paper); }
  .postcard {
    position: relative;
    width: 1200px;
    height: 924px;
    background: var(--paper);
    color: var(--ink);
  }
  .headline {
    position: absolute;
    left: 0;
    top: 0;
    width: 1200px;
    height: 200px;
  }
  .headline text {
    font-family: "Ultra", "Rockwell", serif;
    font-size: 150px;
  }
  .message {
    position: absolute;
    left: 0;
    width: 1220px;
    text-align: center;
    font-family: "Della Respira", "Georgia", serif;
    color: var(--ink);
    line-height: 1;
  }
  .message--tagline { top: 374px; font-size: 92px; letter-spacing: 1px; }
  .message--phone { top: 494px; font-size: 94px; }
  .firm-mark {
    position: absolute;
    left: 40px;
    top: 740px;
    display: flex;
    align-items: center;
    gap: 18px;
  }
  .firm-mark__square {
    width: 140px;
    height: 134px;
    background: var(--brand-ink);
  }
  .firm-mark__name {
    font-family: "Playfair Display", "Georgia", serif;
    font-size: 40px;
    line-height: 1.1;
    color: var(--brand-ink);
  }
  .firm-address {
    position: absolute;
    right: 52px;
    top: 732px;
    text-align: right;
    font-family: "Open Sans", "Segoe UI", sans-serif;
    font-size: 29px;
    line-height: 47px;
    color: var(--ink);
    font-style: normal;
  }
</style>
</head>
<body>
<main class="postcard">
  <svg class="headline" viewBox="0 0 1200 200" aria-label="FORECLOSURE">
    <defs>
      <linearGradient id="headline-fill" x1="0" y1="0" x2="0" y2="1">
        <stop offset="0" stop-color="var(--headline-top)"/>
        <stop offset="0.55" stop-color="#d0150f"/>
        <stop offset="1" stop-color="var(--headline-bottom)"/>
      </linearGradient>
    </defs>
    <text x="29" y="169" textLength="1110" lengthAdjust="spacingAndGlyphs" fill="var(--headline-shadow)">FORECLOSURE</text>
    <text x="25" y="165" textLength="1110" lengthAdjust="spacingAndGlyphs" fill="url(#headline-fill)">FORECLOSURE</text>
  </svg>

  <p class="message message--tagline">You Have Options</p>
  <p class="message message--phone">270-493-2817</p>

  <div class="firm-mark">
    <div class="firm-mark__square"></div>
    <div class="firm-mark__name">Dranford &amp; Pelk, P.S.C.</div>
  </div>

  <address class="firm-address">
    Dranford &amp; Pelk, P.S.C.<br>
    428 Harlow Ridge Road<br>
    Owensboro, KY 42301
  </address>
</main>
</body>
</html>
```